Corvane Health Web Page

We need a visually exciting webpage that introduces people to our practice. We are a practice that has both physiotherapy and psychology and we need the page to reflect this. We are also split across two practice locations. We need the page to be able to be updated regularly to include a blog spot and the linking in of our facebook page. There should be tabs to introduce our practitioners with some blurbs about them, a tab for people to be able to contact us, a tab to read about physiotherapy services and a tab to talk about psychology services. If there are other tabs than please include these. We are a practice that has treated world class athlete on a regular basis and see our selves as leaders in the field and the website must reflect this. I do not want basic clip-arty type things that anyone could have, we have to have something that draws people in.
Updates
Firstly, thanks everyone for their designs. I have attached some links to some physiotherapy websites that I think contain some interesting information and/or layout, as well as some comments,
Hi all,
Reason: Hi Guys,
We are so very close to finding a great design. I feel that we just need a bit of extra time to be able to clinch where we want to be. Thanks for your fantastic designs :)
Regards,
Martin and Ruth
Industry/Entity Type
Health
Requirements
Must have
- 2 Practice Addresses (details to follow for right applications)
Psychology aspect
Physiotherapy aspect
Ability to update blog

```html
<!DOCTYPE html>
<html lang="en">
<head>
<meta charset="utf-8">
<title>Corvane Health – Psychology</title>
<link href="https://fonts.googleapis.com/css2?family=Open+Sans:wght@400;600&family=Questrial&display=swap" rel="stylesheet">
<style>
:root{
  --blue:#1589d9;
  --blue-dark:#0f6fc0;
  --purple:#4a2a8c;
  --purple-deep:#3a1a7a;
  --orange:#f7841e;
  --orange-dark:#e8620a;
  --body-grey:#5f5f5f;
  --rule:#7a7a7a;
  --text-light:#f2f2f2;
  --nav-text:#444;
  --icon-ring:#b9b9c4;
}
*{margin:0;padding:0;box-sizing:border-box}
html,body{width:1200px;height:2211px;overflow:hidden}
body{position:relative;background:var(--body-grey);font-family:'Open Sans',sans-serif;color:var(--text-light)}

.hero{position:absolute;left:0;top:0;width:1200px;height:330px;
  background:linear-gradient(90deg,#2e1f57 0%,#5a3f9e 25%,#7b62b8 45%,#8b5fb0 65%,#6a3d8f 85%,#3b2a5e 100%)}
.hero-lower{position:absolute;left:0;top:187px;width:1200px;height:143px;
  background:linear-gradient(90deg,rgba(120,120,120,.85),rgba(170,170,170,.75) 50%,rgba(110,110,110,.85))}
.hero-rule{position:absolute;left:0;top:185px;width:1200px;border-top:1px dashed rgba(255,255,255,.35)}

.brand{position:absolute;left:187px;top:30px;display:flex;align-items:center;gap:10px}
.brand-mark{width:30px;height:30px;border-radius:50%;background:#fff}
.brand-name{font-family:'Questrial',sans-serif;font-size:36px;color:#fff;line-height:1}
.brand-tag{position:absolute;left:227px;top:72px;font-family:'Questrial',sans-serif;font-size:13px;letter-spacing:2px;color:#fff}

.social{position:absolute;left:837px;top:49px;display:flex;gap:10px}
.social-link{width:37px;height:37px;border-radius:50%;background:#fff;display:flex;align-items:center;justify-content:center}
.social-link::after{content:"";width:25px;height:25px;border-radius:50%;border:1.5px solid var(--icon-ring)}

.nav{position:absolute;left:187px;top:110px;height:40px;display:flex;background:#fff}
.nav a{display:flex;align-items:center;justify-content:center;height:40px;font-family:'Questrial',sans-serif;font-size:16px;color:var(--nav-text);text-decoration:none;border-right:1px solid #ccc}
.nav a:last-child{border-right:0}
.nav a.active{background:var(--blue);color:#fff}

.page-title{position:absolute;left:0;top:214px;width:1200px;text-align:center;font-family:'Questrial',sans-serif;font-weight:400;font-size:46px;color:#fff;letter-spacing:1px}
.page-title::before,.page-title::after{content:"";position:absolute;top:28px;width:160px;border-top:2px solid rgba(255,255,255,.4)}
.page-title::before{left:272px}
.page-title::after{right:272px}
.page-sub{position:absolute;left:0;top:268px;width:1200px;text-align:center;font-family:'Questrial',sans-serif;font-size:17px;color:#fff}

.services{position:absolute;left:0;top:330px;width:1200px;height:1269px;
  background:radial-gradient(ellipse at 50% 30%,#4a4a4a,#303030 75%);border-bottom:1px dashed #888}
.section-head{position:absolute;left:187px;top:55px;width:827px;display:flex;align-items:center;gap:10px;font-family:'Questrial',sans-serif;font-size:19px}
.section-head::after{content:"";flex:1;border-top:2px solid var(--rule)}

.service-grid{position:absolute;left:187px;top:100px;width:827px;display:grid;grid-template-columns:385px 385px;column-gap:57px;grid-auto-rows:140px;row-gap:53.8px}
.service{position:relative;display:flex;gap:15px}
.service:not(.last)::after{content:"";position:absolute;left:0;right:0;bottom:-25px;border-top:2px solid var(--rule)}
.service-photo{width:187px;height:140px;flex:none}
.service h3{font-weight:400;font-size:15px;margin:0 0 4px;color:#fff}
.service p{font-size:11.3px;line-height:13.4px;color:#e6e6e6;width:180px}

.appointment{position:absolute;left:458px;top:1654px;width:290px;height:440px}
.appointment h2{position:absolute;left:25px;top:26px;width:255px;text-align:center;font-family:'Questrial',sans-serif;font-weight:400;font-size:31px;line-height:32px;color:#fff}
.field{position:absolute;left:48px;width:200px;background:#fff;border:2px solid #d8e9f7;font-size:12px;color:#999;padding:5px 8px}
.book{position:absolute;left:48px;top:326px;width:200px;height:44px;background:linear-gradient(var(--orange),var(--orange-dark));color:#fff;font-family:'Questrial',sans-serif;font-size:18px;display:flex;align-items:center;justify-content:center}

.footer{position:absolute;left:0;top:2168px;width:1200px;height:43px;background:var(--blue);font-size:11px;color:#fff}
.footer-links{position:absolute;left:187px;top:14px}
.footer-copy{position:absolute;left:750px;top:14px}
</style>
</head>
<body>

<div class="hero" role="img" aria-label="Gym interior with people exercising, purple tones"></div>
<div class="hero-lower" role="img" aria-label="Blurred gym training scene"></div>
<div class="hero-rule"></div>

<div class="brand"><span class="brand-mark"></span><span class="brand-name">Corvane Health</span></div>
<div class="brand-tag">PHYSIOTHERAPY &amp; PSYCHOLOGY</div>

<div class="social" aria-label="Social links"><span class="social-link"></span><span class="social-link"></span><span class="social-link"></span><span class="social-link"></span></div>

<nav class="nav">
  <a style="width:85px">Home</a>
  <a style="width:102px">About Us</a>
  <a style="width:136px">Physiotherapy</a>
  <a class="active" style="width:109px">Psychology</a>
  <a style="width:149px">Our Practitioners</a>
  <a style="width:128px">Group Classes</a>
  <a style="width:118px">Contact Us</a>
</nav>

<h1 class="page-title">PSYCHOLOGY</h1>
<div class="page-sub">Corvane Health Psychology Services</div>

<section class="services">
  <div class="section-head">Psychology Services</div>
  <div class="service-grid">
    <div class="service"><div class="service-photo" role="img" aria-label="Patient in a therapy session" style="background:linear-gradient(135deg,#6f7378,#3a3d42)"></div><div><h3>Anxiety</h3><p>Lorem ipsum dolor sit amet, consectetur adipiscing elit. In amet fermentum dolor non augue sem pretium egestas. Donec sem eros, at congue ut suere sit amet est. scelerisque viverra odio sit amet laoreet. Nec neque non justo rutrum  dolor sit amet</p></div></div>
    <div class="service"><div class="service-photo" role="img" aria-label="Couple holding hands on a red sofa" style="background:linear-gradient(135deg,#3a4a7a,#b01020)"></div><div><h3>Couples Therapy</h3><p>Lorem ipsum dolor sit amet, consectetur adipiscing elit. In amet fermentum dolor non augue sem pretium egestas. Donec sem eros, at congue ut suere sit amet est. scelerisque viverra odio sit amet laoreet. Nec neque non justo rutrum  dolor sit amet</p></div></div>
    <div class="service"><div class="service-photo" role="img" aria-label="Woman talking with a counsellor" style="background:linear-gradient(135deg,#d8d4cf,#9aa0a6)"></div><div><h3>Depression</h3><p>Lorem ipsum dolor sit amet, consectetur adipiscing elit. In amet fermentum dolor non augue sem pretium egestas. Donec sem eros, at congue ut suere sit amet est. scelerisque viverra odio sit amet laoreet. Nec neque non justo rutrum  dolor sit amet</p></div></div>
    <div class="service"><div class="service-photo" role="img" aria-label="Hands cupping the sunset over the sea" style="background:linear-gradient(180deg,#5c7fa8,#e8a050 60%,#3a3a40)"></div><div><h3>Eating Disorders</h3><p>Lorem ipsum dolor sit amet, consectetur adipiscing elit. In amet fermentum dolor non augue sem pretium egestas. Donec sem eros, at congue ut suere sit amet est. scelerisque viverra odio sit amet laoreet. Nec neque non justo rutrum  dolor sit amet</p></div></div>
    <div class="service"><div class="service-photo" role="img" aria-label="Soldiers standing in formation" style="background:linear-gradient(180deg,#4c6a3a,#8a7a55 60%,#6a5a40)"></div><div><h3>Veteran Counseling</h3><p>Lorem ipsum dolor sit amet, consectetur adipiscing elit. In amet fermentum dolor non augue sem pretium egestas. Donec sem eros, at congue ut suere sit amet est. scelerisque viverra odio sit amet laoreet. Nec neque non justo rutrum  dolor sit amet</p></div></div>
    <div class="service"><div class="service-photo" role="img" aria-label="Man sitting on a bench holding his head" style="background:linear-gradient(180deg,#a0522d,#c9b8a8 55%,#4a6a8a)"></div><div><h3>Pain</h3><p>Lorem ipsum dolor sit amet, consectetur adipiscing elit. In amet fermentum dolor non augue sem pretium egestas. Donec sem eros, at congue ut suere sit amet est. scelerisque viverra odio sit amet laoreet. Nec neque non justo rutrum  dolor sit amet</p></div></div>
    <div class="service"><div class="service-photo" role="img" aria-label="Distressed woman in a family setting" style="background:linear-gradient(135deg,#c8c0b8,#3a2e2a)"></div><div><h3>Family Issues</h3><p>Lorem ipsum dolor sit amet, consectetur adipiscing elit. In amet fermentum dolor non augue sem pretium egestas. Donec sem eros, at congue ut suere sit amet est. scelerisque viverra odio sit amet laoreet. Nec neque non justo rutrum  dolor sit amet</p></div></div>
    <div class="service"><div class="service-photo" role="img" aria-label="Colourful brain inside a head silhouette" style="background:radial-gradient(circle at 50% 45%,#3a6ad0,#102060 55%,#000 90%)"></div><div><h3>Coping with Trauma</h3><p>Lorem ipsum dolor sit amet, consectetur adipiscing elit. In amet fermentum dolor non augue sem pretium egestas. Donec sem eros, at congue ut suere sit amet est. scelerisque viverra odio sit amet laoreet. Nec neque non justo rutrum  dolor sit amet</p></div></div>
    <div class="service"><div class="service-photo" role="img" aria-label="Child blowing a dandelion in a green field" style="background:linear-gradient(90deg,#a06a40,#6abf30 50%,#9ad040)"></div><div><h3>Children Counseling</h3><p>Lorem ipsum dolor sit amet, consectetur adipiscing elit. In amet fermentum dolor non augue sem pretium egestas. Donec sem eros, at congue ut suere sit amet est. scelerisque viverra odio sit amet laoreet. Nec neque non justo rutrum  dolor sit amet</p></div></div>
    <div class="service"><div class="service-photo" role="img" aria-label="Grieving couple with a counsellor" style="background:linear-gradient(135deg,#b08a60,#4a6a9a)"></div><div><h3>Grief</h3><p>Lorem ipsum dolor sit amet, consectetur adipiscing elit. In amet fermentum dolor non augue sem pretium egestas. Donec sem eros, at congue ut suere sit amet est. scelerisque viverra odio sit amet laoreet. Nec neque non justo rutrum  dolor sit amet</p></div></div>
    <div class="service last"><div class="service-photo" role="img" aria-label="Stressed man at a desk" style="background:linear-gradient(180deg,#d8d8d8,#b8a890)"></div><div><h3>Relaxation</h3><p>Lorem ipsum dolor sit amet, consectetur adipiscing elit. In amet fermentum dolor non augue sem pretium egestas. Donec sem eros, at congue ut suere sit amet est. scelerisque viverra odio sit amet laoreet. Nec neque non justo rutrum  dolor sit amet</p></div></div>
    <div class="service last"><div class="service-photo" role="img" aria-label="Teenage girl leaning against a door" style="background:linear-gradient(90deg,#6a5a4a,#2a2420 60%,#1a1614)"></div><div><h3>Teenage Issues</h3><p>Lorem ipsum dolor sit amet, consectetur adipiscing elit. In amet fermentum dolor non augue sem pretium egestas. Donec sem eros, at congue ut suere sit amet est. scelerisque viverra odio sit amet laoreet. Nec neque non justo rutrum  dolor sit amet</p></div></div>
  </div>
</section>

<div class="appointment">
  <svg width="290" height="440" viewBox="0 0 290 440" style="position:absolute;left:0;top:0">
    <polygon points="25,95 2,420 25,415" fill="var(--purple-deep)"/>
    <polygon points="255,415 260,434 230,425" fill="var(--purple)"/>
    <polygon points="25,0 280,0 280,436 152,406 25,436" fill="var(--blue)"/>
  </svg>
  <h2>MAKE AN<br>APPOINTMENT</h2>
  <div class="field" style="top:103px;height:29px">Your Name</div>
  <div class="field" style="top:134px;height:29px">Email ID</div>
  <div class="field" style="top:166px;height:29px">Phone</div>
  <div class="field" style="top:199px;height:118px">Comments</div>
  <div class="book">Book Appointment</div>
</div>

<footer class="footer">
  <div class="footer-links">Home &nbsp;.&nbsp; About us &nbsp;.&nbsp; Practitioners &nbsp;.&nbsp; Our Services &nbsp;.&nbsp; Contact us</div>
  <div class="footer-copy">© 2014 All Right reserved - Terms and Policy</div>
</footer>

</body>
</html>
```